Anzeigengestaltung für Heilpraktikerin für Psychotherapie
Hallo lorvik, ich bin sehr zufrieden mit dem Design. Danke LG Helga Brandner
Zielgruppe
Heilpraktikerin für Psychotherapie, Atem- und Körpertherapeutin, Einzelthearpie, Gruppentherapie, Menschen in Lebenskrisen; Menschen, die ihr Leben verändern wollen, Menschen suchen mehr Selbsterfahrung, vorwiegend Frauen, Atersgruppe 20 aufwärts, Menschen mit psychischen Problemen
Entspannung, Berühren, Massieren, Halten, Gespräch, Bewegen, Begleitung Während der Schwangerschaft, Geburt und danach, Trauerbegleitung
Aufgabenstellung
Name und Berufsbezeichnung sind mir wichtig
Praxiseröffnung, Termine nach Vereinbarung
aktuelles Angebot: Fantasiereise- Entspannung von Alltagsstress
sonstiges Angebot: Einzeltherapie/Gruppentherapie,

```html
<!DOCTYPE html>
<html lang="de">
<head>
<meta charset="utf-8">
<title>Praxiseröffnung – Helga Brandner</title>
<link rel="stylesheet" href="https://fonts.googleapis.com/css2?family=Crimson+Pro:wght@400;600;700&display=swap">
<style>
  :root {
    --sky-top: #ddd2ea;
    --sky-mid: #b3a0d0;
    --sky-low: #8a6fb4;
    --meadow: #2c2434;
    --plum: #6c2b56;
    --plum-text: #6e3a62;
    --magenta: #e0137c;
    --white: #ffffff;
  }
  * { margin: 0; padding: 0; box-sizing: border-box; }
  html, body { width: 800px; height: 1200px; overflow: hidden; background: #ffffff; }
  .ad {
    position: relative;
    width: 800px;
    height: 1200px;
    overflow: hidden;
    font-family: "Crimson Pro", Georgia, serif;
    color: var(--plum-text);
  }
  .backdrop {
    position: absolute;
    inset: 0;
    background: linear-gradient(180deg,
      var(--sky-top) 0%,
      #cfc0e2 30%,
      var(--sky-mid) 58%,
      var(--sky-low) 86%,
      #5f4a80 93%,
      var(--meadow) 100%);
  }
  .brand {
    position: absolute;
    top: 180px;
    left: 0;
    width: 800px;
    text-align: center;
    font-size: 46px;
    font-weight: 400;
    letter-spacing: 2px;
    color: var(--plum);
  }
  .headline {
    position: absolute;
    top: 312px;
    left: 70px;
    font-size: 92px;
    font-weight: 400;
    line-height: 1;
    color: var(--plum);
  }
  .contact {
    position: absolute;
    top: 410px;
    left: 73px;
    font-size: 28px;
    line-height: 36px;
    font-weight: 400;
    list-style: none;
  }
  .contact .name { font-weight: 700; }
  .offer-badge {
    position: absolute;
    left: 102px;
    top: 862px;
    width: 280px;
    height: 280px;
    border-radius: 50%;
    background: var(--magenta);
    color: var(--white);
    text-align: center;
    display: flex;
    flex-direction: column;
    justify-content: center;
  }
  .offer-badge .label { font-size: 24px; line-height: 28px; margin-bottom: 6px; }
  .offer-badge .title { font-size: 34px; line-height: 34px; font-weight: 700; }
  .appointments {
    position: absolute;
    right: 40px;
    top: 1140px;
    font-size: 30px;
    color: var(--white);
  }
</style>
</head>
<body>
  <main class="ad">
    <div class="backdrop" role="img" aria-label="Foto: Silhouette einer Frau mit ausgebreiteten Armen auf einer Wiese vor violettem Abendhimmel"></div>

    <div class="brand">PraxisRaum</div>

    <h1 class="headline">Praxiseröffnung</h1>

    <ul class="contact">
      <li class="name">Helga Brandner</li>
      <li>Heilpraktikerin für Psychotherapie</li>
      <li>Lindenweg 14 / 72418 Talbach</li>
      <li>praxisraum.helgabrandner@postfeld.de</li>
      <li>01720555318 / www.praxisraum-talbach.de</li>
    </ul>

    <div class="offer-badge">
      <p class="label">aktuelles Angebot:</p>
      <p class="title">Fantasiereise-<br>Entspannung<br>vom Alltags-<br>stress</p>
    </div>

    <p class="appointments">Termine nach Vereinbarung</p>
  </main>
</body>
</html>
```